QUICK: Fresh Ideas for New Home Page Design!

Simply improve on our home page design and provide PSD file.

We are Brightpath Coverage, a trusted health insurance comparison site to make shopping and enrolling in Plumwell easy. We are certified agents for Sheltered Pacifica, the state's health insurance marketplace (logo attached).

Use flat UI colors.

Looking for a fun design. Reference websites are:
www.vantrelo.example
www.qubimar.example
www.tolvex.example
www.findmyplan.example
www.marvelcoveragehub.example

Target Market(s)

Individuals ages 18 - 64 shopping for health insurance for themselves and/or their family members. California residents. Don't have health insurance and want it or have it and looking to change.

Industry/Entity Type

Shopping

Font styles to use
Sans Serif

Colors
faed22
33a6d7
33b7a4

Requirements
Must have
• No stock photos. No medical or doctor images or photos. Use images of families. Friendly. Modern fonts and flat UI colors.
Nice to have
• Create a mock-up logo for Brightpath Coverage.
Should not have
• No stock looking photos or images

```html
<!DOCTYPE html>
<html lang="en">
<head>
<meta charset="utf-8">
<title>Brightpath Coverage – Home</title>
<link href="https://fonts.googleapis.com/css2?family=Open+Sans:wght@400;600;700&family=Montserrat:wght@700&display=swap" rel="stylesheet">
<style>
:root{
  --teal:#33b7a4;
  --blue:#33a6d7;
  --yellow:#faed22;
  --ink:#333;
  --muted:#666;
  --pale:#f2f9f8;
  --line:#dfe6e6;
  --white:#fff;
  --page:#fff;
}
*{box-sizing:border-box;margin:0;padding:0}
html,body{width:1200px;height:1000px;overflow:hidden;background:var(--page);font-family:"Open Sans",Arial,sans-serif;color:var(--ink)}
.site{position:absolute;left:436px;top:0;width:328px;height:1000px;overflow:hidden}
.site > *{overflow:hidden}
.topbar{height:11px;background:var(--teal);display:flex;align-items:center;padding:0 18px;font-size:3.2px;color:var(--white);gap:10px;white-space:nowrap}
.topbar .social{margin-left:auto;display:flex;gap:3px}
.topbar .social span{width:4px;height:4px;border-radius:50%;background:var(--white)}
.nav{height:22px;display:flex;align-items:center;padding:0 18px}
.brand{display:flex;align-items:center;gap:3px;font-size:5px;font-weight:700;color:var(--teal);line-height:1;flex:none;width:52px}
.brand .dot{width:11px;height:11px;border-radius:50%;background:var(--blue);flex:none}
.menu{display:flex;gap:7px;font-size:3.6px;font-weight:600;margin-left:auto;white-space:nowrap;align-items:center}
.menu span{flex:none}
.menu .active{border:0.6px solid var(--teal);color:var(--teal);padding:1px 3px}
.hero{height:112px;background:linear-gradient(180deg,#cfe6f4 0%,#e8f2f8 45%,#d9d0c2 75%,#cbbfae 100%);position:relative}
.hero .dots{position:absolute;bottom:5px;left:17px;display:flex;gap:3px}
.hero .dots span{width:3px;height:3px;border-radius:50%;background:#9cc}
.intro{height:74px;text-align:center;padding-top:10px}
.intro h1{font-size:9.5px;font-weight:400;color:#444}
.intro .sub{font-size:6px;color:var(--muted);margin-top:3px}
.intro .call{font-size:8px;color:var(--teal);font-weight:600;margin-top:5px}
.btn{display:inline-block;background:var(--blue);color:var(--white);font-size:5.5px;font-weight:600;padding:2px 5px;margin-top:5px}
.features{height:124px;background:var(--pale);padding-top:11px}
.features h2{text-align:center;font-size:7.5px;font-weight:400;color:var(--teal)}
.feature-grid{display:grid;grid-template-columns:1fr 1fr;column-gap:14px;row-gap:6px;padding:9px 18px 0}
.feature{display:flex;gap:8px}
.feature svg{width:20px;height:20px;flex:none}
.feature h3{font-size:4.6px;font-weight:600;color:#222}
.feature p{font-size:2.8px;color:var(--muted);line-height:1.35;margin-top:1px}
.carriers{height:56px;text-align:center;padding-top:9px}
.carriers h2{font-size:7px;font-weight:600;color:var(--teal)}
.carrier-row{display:flex;align-items:center;justify-content:space-between;padding:9px 8px 0;font-size:5px;font-weight:700;white-space:nowrap}
.carrier-row .arrow{color:#999;font-size:7px;font-weight:400}
.banner{height:98px;background:radial-gradient(ellipse at 50% 90%,#e6f1dd 0%,#7cc3df 40%,#3a9fcd 100%);text-align:center;color:var(--white);padding-top:17px}
.banner h2{font-size:12px;font-weight:400}
.banner .count{font-size:8.5px;font-weight:600;margin-top:3px}
.banner .count em{font-style:normal;color:var(--yellow)}
.banner .sub{font-size:8px;margin-top:3px}
.banner .btn{font-size:6.5px;padding:2px 6px;margin-top:8px}
.team{height:142px;text-align:center;padding-top:10px}
.team h2{font-size:12px;font-weight:400;color:var(--blue)}
.members{display:flex;justify-content:space-between;padding:14px 20px 0}
.member{width:60px}
.member .photo{width:48px;height:48px;border-radius:50%;background:linear-gradient(160deg,#d9d4cc,#7a746c);margin:0 auto}
.member h3{font-size:5.5px;font-weight:400;color:var(--teal);margin-top:6px;letter-spacing:.2px}
.member p{font-size:4.2px;color:#444;line-height:1.3;margin-top:3px}
.newsletter{height:94px;background:var(--pale);text-align:center;padding-top:12px}
.newsletter h2{font-size:7.5px;font-weight:600;color:var(--teal);margin-top:3px}
.newsletter .sub{font-size:5px;color:var(--muted);margin-top:4px}
.subscribe{display:flex;justify-content:center;margin-top:9px}
.subscribe .field{width:142px;height:14px;border:0.6px solid #ccc;border-radius:7px 0 0 7px;background:var(--white);font-size:4.8px;color:#777;text-align:left;padding:3.5px 0 0 10px}
.subscribe .submit{width:42px;height:14px;background:var(--blue);border-radius:0 7px 7px 0;color:var(--white);font-family:"Montserrat",sans-serif;font-weight:700;font-size:5.5px;padding-top:3.5px}
.news{height:222px;text-align:center;padding-top:14px}
.news h2{font-size:11px;font-weight:400;color:var(--blue)}
.news .kicker{font-size:6.5px;color:var(--teal);font-weight:600;margin-top:4px}
.cards{display:grid;grid-template-columns:1fr 1fr;gap:8px 18px;padding:10px 20px 0;text-align:left}
.card{border:0.6px solid var(--line);height:58px;padding:4px 5px;overflow:hidden}
.card h3{font-size:4.2px;font-weight:600}
.card .meta{font-size:2.7px;color:var(--muted);margin-top:3px}
.card p{font-size:2.7px;color:var(--muted);line-height:1.35;margin-top:3px}
.card .more{font-size:2.8px;margin-top:3px;font-weight:600;color:var(--ink)}
.card .likes{font-size:2.8px;margin-top:3px;display:flex;align-items:center;gap:2px}
.card .likes span{width:3px;height:3px;border-radius:50%;background:var(--yellow)}
.disclaimer{height:26px;font-size:2.6px;color:var(--muted);line-height:1.45;text-align:center;padding:4px 22px 0}
.footer{height:11px;background:var(--teal);display:flex;align-items:center;padding:0 20px;gap:6px;font-size:3.4px;color:var(--white);white-space:nowrap}
.footer .social{margin-left:auto;display:flex;gap:3px}
.footer .social span{width:3.5px;height:3.5px;border-radius:50%;background:var(--white)}
.copyright{height:8px;font-size:3px;color:var(--muted);text-align:center;padding-top:3px}
</style>
</head>
<body>
<div class="site">
  <div class="topbar">
    <span>14085 Lorem ipsum dolor sit amet</span>
    <span>1-800-555-0142</span>
    <span>info@vantrelo.example</span>
    <div class="social"><span></span><span></span><span></span><span></span><span></span></div>
  </div>

  <header class="nav">
    <div class="brand"><span class="dot"></span><span>Sheltered<br>Pacifica</span></div>
    <nav class="menu">
      <span class="active">HOME</span><span>ABOUT US</span><span>DO I QUALIFY?</span><span>APPLY</span><span>HEALTH PLANS</span><span>COVERAGE</span><span>EMPLOYERS</span><span>NEWS</span><span>FAQ</span><span>GET HELP</span>
    </nav>
  </header>

  <section class="hero" role="img" aria-label="Photo of a family walking hand in hand along a sunny beach">
    <div class="dots"><span></span><span style="background:#3aa"></span><span></span><span></span></div>
  </section>

  <section class="intro">
    <h1>You Can Still Apply for Health Coverage!</h1>
    <p class="sub">Affordable health coverage is available all year</p>
    <p class="call">Apply now or call us at 1-800-555-0142 to learn more!</p>
    <span class="btn">Get A Quote</span>
  </section>

  <section class="features">
    <h2>Health Insurance Doesn't Have to be Complicated</h2>
    <div class="feature-grid">
      <div class="feature">
        <svg viewBox="0 0 20 20"><g fill="#33a6d7"><rect x="2" y="14" width="3" height="4"/><rect x="6" y="11" width="3" height="7"/><rect x="10" y="8" width="3" height="10"/><rect x="14" y="5" width="3" height="13"/></g><path d="M2 12 L8 7 L11 9 L17 3" stroke="#33a6d7" fill="none" stroke-width="1"/></svg>
        <div><h3>We help you get financial assistance</h3><p>Lorem ipsum dolor sit amet, consectetur adipiscing elit. Etiam eget urna non orci elementum vulputate eu ac elit. Etiam in tempor massa egestas justo.</p></div>
      </div>
      <div class="feature">
        <svg viewBox="0 0 20 20"><rect x="6" y="2" width="9" height="16" rx="1.5" fill="none" stroke="#33a6d7" stroke-width="1.2"/><circle cx="10.5" cy="15.5" r="0.9" fill="#33a6d7"/><path d="M8 9 l2 2 l3-4" stroke="#33a6d7" fill="none" stroke-width="1"/></svg>
        <div><h3>We help you enroll</h3><p>Lorem ipsum dolor sit amet, consectetur adipiscing elit. Etiam eget urna non orci elementum vulputate eu ac elit. Etiam in tempor massa egestas justo.</p></div>
      </div>
      <div class="feature">
        <svg viewBox="0 0 20 20"><circle cx="10" cy="8" r="5" fill="none" stroke="#33a6d7" stroke-width="1.1"/><rect x="8" y="13.5" width="4" height="3" fill="#33a6d7"/><g stroke="#33a6d7" stroke-width="0.8"><path d="M10 0.5v1.5M3 8H1.5M18.5 8H17M4.5 2.5l1 1M15.5 2.5l-1 1"/></g></svg>
        <div><h3>We help you choose the right plan</h3><p>Lorem ipsum dolor sit amet, consectetur adipiscing elit. Etiam eget urna non orci elementum vulputate eu ac elit. Etiam in tempor massa egestas justo.</p></div>
      </div>
      <div class="feature">
        <svg viewBox="0 0 20 20"><circle cx="10" cy="10" r="7.5" fill="none" stroke="#33a6d7" stroke-width="1.2"/><path d="M13.5 6.5 L11 11 L6.5 13.5 L9 9 Z" fill="#33a6d7"/></svg>
        <div><h3>We navigate you through health reform</h3><p>Lorem ipsum dolor sit amet, consectetur adipiscing elit. Etiam eget urna non orci elementum vulputate eu ac elit. Etiam in tempor massa egestas justo.</p></div>
      </div>
      <div class="feature">
        <svg viewBox="0 0 20 20"><path d="M1 9 L6 6 L10 8 L14 6 L19 9 L15 14 L10 15 L5 14 Z" fill="#33a6d7"/><path d="M7 10 L10 12 L13 10" stroke="#fff" fill="none" stroke-width="0.8"/></svg>
        <div><h3>We make sure you get the best deal possible</h3><p>Lorem ipsum dolor sit amet, consectetur adipiscing elit. Etiam eget urna non orci elementum vulputate eu ac elit. Etiam in tempor massa egestas justo.</p></div>
      </div>
      <div class="feature">
        <svg viewBox="0 0 20 20"><circle cx="10" cy="7" r="4" fill="#33a6d7"/><path d="M3 18 C3 13 6 12 10 12 C14 12 17 13 17 18 Z" fill="#33a6d7"/></svg>
        <div><h3>We're always here to help</h3><p>Lorem ipsum dolor sit amet, consectetur adipiscing elit. Etiam eget urna non orci elementum vulputate eu ac elit. Etiam in tempor massa egestas justo.</p></div>
      </div>
    </div>
  </section>

  <section class="carriers">
    <h2>CHOOSE FROM OVER 300 CARRIERS INCLUDING</h2>
    <div class="carrier-row">
      <span class="arrow">‹</span>
      <span style="color:#7a2a8f">Alderic</span>
      <span style="color:#3d6fb5">Tressan Care</span>
      <span style="color:#1e5aa8">Orvillo Health</span>
      <span style="color:#1f8ab8">Kestrel Mutual</span>
      <span style="color:#4aa53a">Halvane</span>
      <span style="color:#2c5f9e">Pinecrest Community</span>
      <span style="color:#555">Solmar</span>
      <span class="arrow">›</span>
    </div>
  </section>

  <section class="banner">
    <h2>You Can Still Apply for Health Coverage!</h2>
    <p class="count">10,000+ <em>Plans From</em> 200+ <em>Carriers</em></p>
    <p class="sub">Affordable health coverage is available all year</p>
    <span class="btn">Shop Now</span>
  </section>

  <section class="team">
    <h2>OUR TEAM</h2>
    <div class="members">
      <div class="member"><div class="photo" role="img" aria-label="Portrait of a male licensed agent"></div><h3>LOREM IPSUM</h3><p>Licensed agent since 2009 Individual &amp; Family health insurance</p></div>
      <div class="member"><div class="photo" role="img" aria-label="Portrait of a female licensed agent" style="background:linear-gradient(160deg,#f0e4c8,#b59a6a)"></div><h3>REM PSUM</h3><p>Licensed agent since 2009 Individual &amp; Family health insurance</p></div>
      <div class="member"><div class="photo" role="img" aria-label="Portrait of a male licensed agent" style="background:linear-gradient(160deg,#ddd,#333)"></div><h3>BLANDIT FRING</h3><p>Licensed agent since 2009 Individual &amp; Family health insurance</p></div>
      <div class="member"><div class="photo" role="img" aria-label="Portrait of a female licensed agent" style="background:linear-gradient(160deg,#efe6d2,#8d7a5a)"></div><h3>SUSPE SOLLIC</h3><p>Licensed agent since 2009 Individual &amp; Family health insurance</p></div>
    </div>
  </section>

  <section class="newsletter">
    <svg width="14" height="10" viewBox="0 0 14 10"><rect x="0.5" y="0.5" width="13" height="9" fill="none" stroke="#faed22" stroke-width="1"/><path d="M0.5 0.5 L7 5.5 L13.5 0.5" fill="none" stroke="#faed22" stroke-width="1"/></svg>
    <h2>Get Notified of any updates!</h2>
    <p class="sub">Subscribe to our newsletter to be notified about new version release</p>
    <div class="subscribe"><div class="field">Your email address</div><div class="submit">SUBMIT</div></div>
  </section>

  <section class="news">
    <h2>NEWS</h2>
    <p class="kicker">THE LATEST ON SHELTERED PACIFICA PLUMWELL</p>
    <div class="cards">
      <article class="card"><h3>Why Are My Children On Medi-Plan? What are My Options?</h3><p class="meta">08 August | Sheltered Pacifica | Dana Whitlow | No comment</p><p>We receive numerous phone calls asking about Medi-Plan for children. Unfortunately, due to funding issues, the state is still processing many applications for Medi-Plan. You can tell many of you without ID cards for children that need a doctor.</p><p class="more">Read more →</p><p class="likes"><span></span>8</p></article>
      <article class="card"><h3>Why Are My Children On Medi-Plan? What are My Options?</h3><p class="meta">08 August | Sheltered Pacifica | Dana Whitlow | No comment</p><p>We receive numerous phone calls asking about Medi-Plan for children. Unfortunately, due to funding issues, the state is still processing many applications for Medi-Plan. You can tell many of you without ID cards for children that need a doctor.</p><p class="more">Read more →</p><p class="likes"><span></span>1</p></article>
      <article class="card"><h3>Why Are My Children On Medi-Plan? What are My Options?</h3><p class="meta">08 August | Sheltered Pacifica | Dana Whitlow | No comment</p><p>We receive numerous phone calls asking about Medi-Plan for children. Unfortunately, due to funding issues, the state is still processing many applications for Medi-Plan. You can tell many of you without ID cards for children that need a doctor.</p><p class="more">Read more →</p><p class="likes"><span></span>6</p></article>
      <article class="card"><h3>Why Are My Children On Medi-Plan? What are My Options?</h3><p class="meta">08 August | Sheltered Pacifica | Dana Whitlow | No comment</p><p>We receive numerous phone calls asking about Medi-Plan for children. Unfortunately, due to funding issues, the state is still processing many applications for Medi-Plan. You can tell many of you without ID cards for children that need a doctor.</p><p class="more">Read more →</p><p class="likes"><span></span>2</p></article>
    </div>
  </section>

  <p class="disclaimer">"Sheltered Pacifica" and the Sheltered Pacifica logo are registered trademarks or service marks of Sheltered Pacifica, in the United States. This website is owned and maintained by Brightpath Coverage Insurance Services Inc., which is solely responsible for its content. The site is not maintained by or affiliated with Sheltered Pacifica, and Sheltered Pacifica bears no responsibility for its content. The e-mail addresses and telephone numbers that appear throughout this site belong to Brightpath Coverage Insurance Services Inc. and cannot be used to contact Sheltered Pacifica.</p>

  <footer class="footer">
    <span>Home</span><span>About Us</span><span>Do I Qualify</span><span>Apply</span><span>Health Plans</span><span>Coverage</span><span>Employers</span><span>News</span><span>Faq</span><span>Get Help</span>
    <div class="social"><span></span><span></span><span></span><span></span></div>
  </footer>
  <p class="copyright">©2014, Brightpath Coverage Insurance Services Inc. CA License Number 0F00000</p>
</div>
</body>
</html>
```